Lumo Tavi Menu Design Project

This project is pretty straight forward. You will be given 3 files which include the following:
1. Our proposed menu
2. Our Company logo
3. A sample menu on what we are looking for design wise

Your job is to create a visually pleasing menu that is simple, clean and fresh. Please refer to our home website for additional information. (www.lumotavi.example) Must be in eps or equivalent format.

Target Market(s)

20s to 40s

Industry/Entity Type

It Company

Requirements
Must have
• Company log
Must be in EPS format

```html
<!DOCTYPE html>
<html lang="en">
<head>
<meta charset="utf-8">
<title>Lumo Tavi — Noodles, Tea &amp; Beverages</title>
<link rel="stylesheet" href="https://fonts.googleapis.com/css2?family=Jost:ital,wght@0,400;0,500;1,400&display=swap">
<style>
  :root {
    --ink: #ffffff;
    --bg: #000000;
    --red: #c8232b;
    --emblem: #5c0c10;
  }
  * { margin: 0; padding: 0; box-sizing: border-box; }
  html, body { width: 1200px; height: 1000px; overflow: hidden; background: var(--bg); }
  .menu {
    position: relative;
    width: 1200px; height: 1000px;
    background: var(--bg);
    color: var(--ink);
    font-family: "Jost", sans-serif;
    overflow: hidden;
  }
  .emblem { position: absolute; left: 100px; top: 110px; width: 820px; height: 620px; }
  .section-title {
    position: absolute;
    color: var(--red);
    font-weight: 400;
    font-size: 25px;
    letter-spacing: 0.5px;
    text-transform: uppercase;
    text-align: center;
  }
  .title-noodles { left: 54px; width: 486px; top: 10px; }
  .title-tea { left: 620px; width: 544px; top: 10px; }
  .title-beverages { left: 0; width: 1200px; top: 674px; }
  .rule-vertical { position: absolute; left: 601px; top: 22px; width: 3px; height: 640px; background: var(--red); }
  .rule-horizontal { position: absolute; left: 40px; top: 661px; width: 1113px; height: 3px; background: var(--red); }
  .column { position: absolute; }
  .column-noodles { left: 54px; top: 62px; width: 486px; font-size: 17px; line-height: 20px; }
  .column-tea { left: 665px; top: 61px; width: 484px; height: 600px; overflow: hidden; font-size: 17px; line-height: 21.2px; }
  .item-head { display: flex; justify-content: space-between; font-weight: 500; }
  .item-desc { font-style: italic; text-align: right; font-weight: 400; }
  .column-tea .item-desc { text-align: right; }
  .drinks { position: absolute; top: 714px; font-size: 17px; line-height: 21.5px; }
  .drinks-left { left: 54px; width: 494px; }
  .drinks-right { left: 661px; width: 488px; }
  .drink { margin-bottom: 20px; }
  .drink.tight { margin-bottom: 0; }
  .drink-row { display: flex; justify-content: space-between; }
  .drink-row.size { font-style: italic; }
  .drink-row.size .price { font-style: normal; font-weight: 500; }
  .drink-name, .price { font-weight: 500; }
  .drink-note { font-style: italic; text-align: right; }
  .brand {
    position: absolute; top: 936px;
    display: flex; align-items: center; gap: 6px;
    color: var(--red); font-weight: 500; font-size: 15px; letter-spacing: 0.5px;
  }
  .brand-left { left: 24px; }
  .brand-right { right: 24px; }
  .brand-square { width: 10px; height: 10px; background: var(--red); }
</style>
</head>
<body>
<main class="menu">
  <svg class="emblem" role="img" aria-label="Large faint red swirl emblem behind the menu" viewBox="0 0 820 620">
    <defs>
      <radialGradient id="emblem-glow" cx="50%" cy="50%" r="50%">
        <stop offset="0%" stop-color="var(--emblem)" stop-opacity="0.9"/>
        <stop offset="70%" stop-color="var(--emblem)" stop-opacity="0.55"/>
        <stop offset="100%" stop-color="var(--emblem)" stop-opacity="0"/>
      </radialGradient>
    </defs>
    <ellipse cx="410" cy="310" rx="400" ry="300" fill="url(#emblem-glow)"/>
  </svg>

  <h2 class="section-title title-noodles">Noodles</h2>
  <h2 class="section-title title-tea">Leaf &amp; Kettle by the Pot</h2>
  <div class="rule-vertical"></div>
  <div class="rule-horizontal"></div>

  <section class="column column-noodles">
    <div class="item"><div class="item-head"><span>Lo Mein</span><span>10.95</span></div>
      <p class="item-desc">Soft lo mein noodles with shredded vegetables and<br>chicken, pork, or vegetables.<br>Beef or shrimp instead, add $1.00.</p></div>
    <div class="item"><div class="item-head"><span>Chow Mein</span><span>12.95</span></div>
      <p class="item-desc">Crispy egg noodles or soft lo mein noodles with large<br>vegetables and chicken, pork, or vegetables.<br>Beef or shrimp instead, add $1.00.</p></div>
    <div class="item"><div class="item-head"><span>Pad Thai</span><span>12.95</span></div>
      <p class="item-desc">Rice noodles with chicken, shrimp, eggs, onions, and<br>scallions topped with peanuts and cilantro.</p></div>
    <div class="item"><div class="item-head"><span>Peanut Noodles</span><span>8.95</span></div>
      <p class="item-desc">Soft lo mein noodles with scallions, chopped peanuts,<br>preserved szechwan vegetables, and a spicy peanut<br>sauce.<br>Add chicken $2.00.</p></div>
    <div class="item"><div class="item-head"><span>Mira’s Noodles</span><span>9.95</span></div>
      <p class="item-desc">Lo mein noodles with sliced chicken breast in a spicy<br>cilantro sauce.</p></div>
    <div class="item"><div class="item-head"><span>Singapore Noodles</span><span>10.95</span></div>
      <p class="item-desc">Shrimp, barbeque pork, bean sprouts, onions, egg, and<br>bell peppers with rice noodles in a curry sauce.</p></div>
    <div class="item"><div class="item-head"><span>Chow Fun</span><span>10.95</span></div>
      <p class="item-desc">Chicken, pork, or vegetables with bean sprouts, scallions,<br>onions, and wide rice noodles. For beef or shrimp in-<br>stead, add $1.00.</p></div>
  </section>

  <section class="column column-tea">
    <div class="item"><div class="item-head"><span>Green Kukicha Tea</span><span>3.75</span></div>
      <p class="item-desc">Often enjoyed for its health benefits, this tea has a fresh<br>green, grassy taste with a crisp finish.</p></div>
    <div class="item"><div class="item-head"><span>Ginger Ginseng Tea</span><span>3.75</span></div>
      <p class="item-desc">This unique chamomile blend is velvety, yet mellow with a<br>complex finish of cinnamon, apple, and lime. Caffeine-<br>Free.</p></div>
    <div class="item"><div class="item-head"><span>White Coconut Crème</span><span>3.75</span></div>
      <p class="item-desc">Tender white peony leaves blended with cornflower, saf-<br>flower, and sweet creamy coconut.</p></div>
    <div class="item"><div class="item-head"><span>Wuyi Oolong Tea</span><span>3.75</span></div>
      <p class="item-desc">Long beautiful leaves unwind and unfurl when steeped<br>to release a smooth, rice flavor with crisp and earthy<br>tones.</p></div>
    <div class="item"><div class="item-head"><span>Premium Halo Tea</span><span>4.25</span></div>
      <p class="item-desc">Hand-Tied white tea blossoms into a rainbow of jasmine<br>and amaranth flowers with fresh fruit notes.</p></div>
    <div class="item"><div class="item-head"><span>Fjell Water</span><span>0.00</span></div>
      <p class="item-desc">Sparkling or flat. Small 375 ml $4.00.Large 800 ml $6.00.</p></div>
    <div class="item"><div class="item-head"><span>Jasmine Reserve Tea</span><span>3.75</span></div>
      <p class="item-desc">Organic fair trade green tea repeatedly baked and<br>scented with fresh and fragrant jasmine blossoms.</p></div>
    <div class="item"><div class="item-head"><span>English Breakfast Tea</span><span>3.75</span></div>
      <p class="item-desc">A smooth malty brew with a clean finish, this is leaf &amp;<br>kettle’s traditional blend of organic black tea.</p></div>
    <div class="item"><div class="item-head"><span>Chamomile Clementine Tea</span><span>3.75</span></div>
      <p class="item-desc">This unique chamomile blend is velvety, yet mellow with a<br>complex finish of cinnamon, apple, and lime. Caffeine-</p></div>
  </section>

  <h2 class="section-title title-beverages">Beverages</h2>

  <section class="drinks drinks-left">
    <div class="drink">
      <div class="drink-row"><span class="drink-name">FJELL (Sparkling or Still)</span></div>
      <div class="drink-row size"><span>Small (375ml</span><span class="price">4.00</span></div>
      <div class="drink-row size"><span>Large (800ml)</span><span class="price">6.50</span></div>
    </div>
    <div class="drink tight">
      <div class="drink-row"><span class="drink-name">Cola</span><span class="price">2.75</span></div>
      <p class="drink-note">Cola, Diet Cola, Lemon-Lime Soda, Cherry Cola, Orange Soda</p>
    </div>
    <div class="drink">
      <div class="drink-row"><span class="drink-name">Lemonade</span><span class="price">3.50</span></div>
    </div>
  </section>

  <section class="drinks drinks-right">
    <div class="drink">
      <div class="drink-row"><span class="drink-name">Orange &amp; Cranberry Juice</span><span class="price">3.50</span></div>
    </div>
    <div class="drink">
      <div class="drink-row"><span class="drink-name">Ember Forge French Press Coffee</span><span class="price">3.95</span></div>
      <p class="drink-note">Caffeinated or Decaffeinated</p>
    </div>
    <div class="drink">
      <div class="drink-row"><span class="drink-name">Iced Teas</span><span class="price">2.75</span></div>
      <p class="drink-note">Traditional, Mango, Blackberry Jasmine Green</p>
    </div>
  </section>

  <div class="brand brand-left"><span class="brand-square"></span><span>Lumo Tavi</span></div>
  <div class="brand brand-right"><span class="brand-square"></span><span>Lumo Tavi</span></div>
</main>
</body>
</html>
```